Business card and stationery for an eCommerce store
Vornel Home Solutions
Business card and stationery for an eCommerce store - Retailers
Creative Brief
Simple
Tarin Velo K.M
Managing Partner
Vornel Home Solutions #254 , 6th B Cross, G D Layout, Hosadiga Ext, Kelnavadi, Bangalore - 560481
pkelmandro@vomta.in
www.vomta.in
Vornel Home Solutions is the private limited firm that owns vomta.in. Vornel Home Solutions doesn't have any separate identity/ logo created. In addition to business card design, I would also like to see designs for Letterhead and Envelope.
Concepts
Business Cards/Letterhead/ Envelopes/Notepads/Tshirt/labels for copper kite crate

```html
<!DOCTYPE html>
<html lang="en">
<head>
<meta charset="utf-8">
<title>vomta.in Stationery Set</title>
<link href="https://fonts.googleapis.com/css2?family=Open+Sans:wght@400;700;800&display=swap" rel="stylesheet">
<style>
  :root {
    --bg: #000000;
    --paper: #ffffff;
    --orange: #f7941d;
    --red: #c1272d;
    --deep-red: #b5121b;
    --ink: #555555;
  }
  html, body {
    margin: 0;
    padding: 0;
    width: 1200px;
    height: 768px;
    overflow: hidden;
    background: var(--bg);
  }
  .stationery-set {
    display: block;
    width: 1200px;
    height: 768px;
    font-family: "Open Sans", Arial, sans-serif;
  }
  .paper { fill: var(--paper); }
  .band { fill: var(--orange); }
  .band-line { fill: none; stroke: var(--red); stroke-width: 3; }
  .brand { font-weight: 800; fill: var(--orange); }
  .brand-mark { fill: var(--red); }
  .brand-white { font-weight: 800; fill: var(--paper); }
  .footer-text { fill: var(--paper); font-size: 9px; }
  .card-name { fill: var(--red); font-weight: 700; font-size: 9px; }
  .card-role { fill: var(--ink); font-size: 7px; }
  .card-line { fill: var(--ink); font-size: 6px; }
  .card-orange { fill: var(--orange); }
  .card-red { fill: var(--deep-red); }
</style>
</head>
<body>
<svg class="stationery-set" viewBox="0 0 1200 768" xmlns="http://www.w3.org/2000/svg">

  <!-- Letterhead -->
  <g class="letterhead">
    <rect class="paper" x="53" y="31" width="506" height="660"/>
    <rect class="brand-mark" x="68" y="58" width="10" height="10"/>
    <text class="brand" x="84" y="78" font-size="34">vomta.in</text>
    <path class="band" d="M53,568 C180,530 380,600 559,548 L559,691 L53,691 Z"/>
    <path class="band-line" d="M53,566 C180,528 380,598 559,546"/>
    <g class="footer-text">
      <text x="70" y="606">Vornel Home Solutions</text>
      <text x="70" y="619">#254 , 6th B Cross,</text>
      <text x="70" y="632">G D Layout, Hosadiga Ext,</text>
      <text x="70" y="645">Kelnavadi, Bangalore - 560481</text>
      <text x="70" y="658">Phone: 080-41234567 | Cell: 98450 12345</text>
      <text x="70" y="671">Email: pkelmandro@vomta.in | www.vomta.in</text>
    </g>
  </g>

  <!-- Business card front -->
  <g class="card-front">
    <rect class="paper" x="590" y="34" width="207" height="112" rx="6"/>
    <rect class="brand-mark" x="600" y="46" width="7" height="7"/>
    <text class="brand" x="611" y="64" font-size="24">vomta.in</text>
    <text class="card-name" x="720" y="84">Tarin Velo K.M</text>
    <text class="card-role" x="722" y="94">Managing Partner</text>
    <text class="card-line" x="600" y="84">Vornel Home Solutions</text>
    <text class="card-line" x="600" y="92">#254 , 6th B Cross, G D Layout,</text>
    <text class="card-line" x="600" y="100">Hosadiga Ext, Kelnavadi - 560481</text>
    <text class="card-line" x="600" y="108">pkelmandro@vomta.in</text>
    <path class="band" d="M590,128 C650,112 740,136 797,118 L797,140 Q797,146 791,146 L596,146 Q590,146 590,140 Z"/>
    <path class="band-line" d="M590,127 C650,111 740,135 797,117" stroke-width="2"/>
  </g>

  <!-- Business card back, white -->
  <g class="card-back-white">
    <rect class="paper" x="878" y="79" width="209" height="118" rx="8"/>
    <text class="brand" x="982" y="145" font-size="26" text-anchor="middle">vomta.in</text>
  </g>

  <!-- Business card back, orange -->
  <g class="card-back-orange">
    <rect class="card-orange" x="653" y="192" width="209" height="120" rx="8"/>
    <text class="brand-white" x="757" y="260" font-size="26" text-anchor="middle">vomta.in</text>
  </g>

  <!-- Business card back, red -->
  <g class="card-back-red">
    <rect class="card-red" x="907" y="240" width="209" height="120" rx="8"/>
    <text class="brand-white" x="1011" y="308" font-size="26" text-anchor="middle">vomta.in</text>
  </g>

  <!-- Envelope -->
  <g class="envelope">
    <rect class="paper" x="590" y="372" width="552" height="317" rx="10"/>
    <path class="band" d="M600,372 L1132,372 Q1142,372 1142,382 L1142,420 C1040,440 930,470 866,482 C800,470 690,440 590,420 L590,382 Q590,372 600,372 Z"/>
    <path class="band-line" d="M1142,420 C1040,440 930,470 866,482 C800,470 690,440 590,420" stroke-width="2"/>
    <text class="brand-white" x="866" y="430" font-size="12" text-anchor="middle">vomta.in</text>
    <rect class="brand-mark" x="612" y="496" width="10" height="10"/>
    <text class="brand" x="628" y="518" font-size="36">vomta.in</text>
    <path class="band" d="M590,618 C700,580 900,640 1142,596 L1142,679 Q1142,689 1132,689 L600,689 Q590,689 590,679 Z"/>
    <path class="band-line" d="M590,616 C700,578 900,638 1142,594"/>
    <g class="footer-text">
      <text x="610" y="640">Vornel Home Solutions</text>
      <text x="610" y="652">#254 , 6th B Cross,</text>
      <text x="610" y="664">G D Layout, Hosadiga Ext,</text>
      <text x="610" y="676">Kelnavadi, Bangalore - 560481</text>
    </g>
  </g>
</svg>
</body>
</html>
```